Business Card for Mortuary

We need a business card design for our mortuary. We are not the "traditional" mortuary and specialize in simple cremations and burials. We use a two sided card.

Industry/Entity Type

Funeral Home

Contact Information for Business Card

One side we would like to have with the general information of the mortuary:
Address: 4172 E. Larkspur Ave, Sun City, AZ 85904
Phone: 623-555-0148
email: hello@willowmereplace.com
website: willowmereplace.com

On the other side would like to have the information of employee:
Name: Peter K. Lund
Email: peter@willowmereplace.com
Title: Funeral Director
Text: 602-555-0173

Font styles to use
Serif
Sans Serif

Requirements
Should not have
• Do not put any gothic images or things like a hearse or tombstone.

```html
<!DOCTYPE html>
<html lang="en">
<head>
<meta charset="utf-8">
<title>Willowmere Place – Business Cards</title>
<link rel="stylesheet" href="https://fonts.googleapis.com/css2?family=Lato:wght@400;700;900&display=swap">
<style>
  :root {
    --backdrop: #3a3b3e;
    --card: #ffffff;
    --ink: #141414;
    --leaf: #7dc242;
    --leaf-line: #a9d880;
    --tab-edge: #1d2a12;
  }
  * { box-sizing: border-box; margin: 0; padding: 0; }
  html, body {
    width: 1200px; height: 900px; overflow: hidden;
    background: var(--backdrop);
    font-family: "Lato", Arial, sans-serif;
    color: var(--ink);
  }
  .stage { position: relative; width: 1200px; height: 900px; }
  .card {
    position: absolute;
    width: 560px; height: 320px;
    background: var(--card);
    border-radius: 28px;
    overflow: hidden;
    box-shadow: 0 14px 30px rgba(0,0,0,.35);
  }
  .card--company { left: 60px; top: 80px; }
  .card--staff { left: 580px; top: 490px; }

  .brand {
    position: absolute; top: 46px; left: 0; right: 0;
    display: flex; justify-content: center; align-items: center; gap: 14px;
  }
  .brand__mark { display: flex; align-items: center; gap: 10px; }
  .brand__dot { width: 30px; height: 30px; border-radius: 50%; background: var(--leaf); }
  .brand__name {
    font-weight: 900; font-size: 30px; line-height: .95;
    text-transform: uppercase; color: var(--ink); letter-spacing: .5px;
  }
  .brand__tagline {
    border-left: 1.5px solid var(--leaf);
    padding-left: 8px;
    font-size: 14px; line-height: 1.15; color: var(--leaf);
  }

  .details { position: absolute; top: 128px; left: 0; right: 0; text-align: center; }
  .address { font-size: 15px; line-height: 1.35; }
  .person__name { font-size: 28px; font-weight: 900; color: var(--leaf); line-height: 1.05; }
  .person__title { font-size: 15px; margin-top: 2px; }

  .divider {
    display: flex; justify-content: center; align-items: center; gap: 6px;
    margin: 10px auto 8px;
  }
  .divider__rule { width: 70px; height: 1px; background: var(--leaf-line); }
  .divider__icon { width: 18px; height: 18px; }

  .contact { font-size: 15px; line-height: 1.45; }

  .web-tab { position: absolute; bottom: 0; left: 250px; width: 240px; height: 42px; }
  .web-tab__label {
    position: absolute; bottom: 0; left: 250px; width: 200px; height: 38px;
    display: flex; align-items: center; justify-content: center;
    color: #fff; font-size: 14px; letter-spacing: .3px;
  }
</style>
</head>
<body>
<main class="stage">

  <section class="card card--company">
    <header class="brand">
      <div class="brand__mark">
        <span class="brand__dot"></span>
        <span class="brand__name">Willowmere<br>Place</span>
      </div>
      <div class="brand__tagline">Affordable<br>Cremation<br>and Burial</div>
    </header>

    <div class="details">
      <p class="address">4172 E. Larkspur Ave,<br>Sun City, AZ 85904</p>
      <div class="divider">
        <span class="divider__rule"></span>
        <svg class="divider__icon" viewBox="0 0 18 18" aria-hidden="true"><circle cx="9" cy="9" r="8" fill="var(--leaf)"/><path d="M6 5l2 2-1 1c.5 1.2 1.5 2.2 3 3l1-1 2 2-1.2 1.2C9 13 5 9 4.8 6.2z" fill="#fff"/></svg>
        <svg class="divider__icon" viewBox="0 0 18 18" aria-hidden="true"><circle cx="9" cy="9" r="8" fill="var(--leaf)"/><rect x="4.5" y="6" width="9" height="6.5" fill="none" stroke="#fff" stroke-width="1.2"/><path d="M4.5 6l4.5 3.6L13.5 6" fill="none" stroke="#fff" stroke-width="1.2"/></svg>
        <span class="divider__rule"></span>
      </div>
      <p class="contact">623-555-0148<br>hello@willowmereplace.com</p>
    </div>

    <svg class="web-tab" viewBox="0 0 240 42" aria-hidden="true">
      <path d="M0 42V12Q0 3 9 3H188Q194 3 198 7L240 42Z" fill="var(--leaf)" stroke="var(--tab-edge)" stroke-width="1.5"/>
    </svg>
    <span class="web-tab__label">www.willowmereplace.com</span>
  </section>

  <section class="card card--staff">
    <header class="brand">
      <div class="brand__mark">
        <span class="brand__dot"></span>
        <span class="brand__name">Willowmere<br>Place</span>
      </div>
      <div class="brand__tagline">Affordable<br>Cremation<br>and Burial</div>
    </header>

    <div class="details">
      <p class="person__name">Peter K. Lund</p>
      <p class="person__title">Funeral Director</p>
      <div class="divider">
        <span class="divider__rule"></span>
        <svg class="divider__icon" viewBox="0 0 18 18" aria-hidden="true"><circle cx="9" cy="9" r="8" fill="var(--leaf)"/><path d="M6 5l2 2-1 1c.5 1.2 1.5 2.2 3 3l1-1 2 2-1.2 1.2C9 13 5 9 4.8 6.2z" fill="#fff"/></svg>
        <svg class="divider__icon" viewBox="0 0 18 18" aria-hidden="true"><circle cx="9" cy="9" r="8" fill="var(--leaf)"/><rect x="4.5" y="6" width="9" height="6.5" fill="none" stroke="#fff" stroke-width="1.2"/><path d="M4.5 6l4.5 3.6L13.5 6" fill="none" stroke="#fff" stroke-width="1.2"/></svg>
        <span class="divider__rule"></span>
      </div>
      <p class="contact">602-555-0173<br>peter@willowmereplace.com</p>
    </div>

    <svg class="web-tab" viewBox="0 0 240 42" aria-hidden="true">
      <path d="M0 42V12Q0 3 9 3H188Q194 3 198 7L240 42Z" fill="var(--leaf)" stroke="var(--tab-edge)" stroke-width="1.5"/>
    </svg>
    <span class="web-tab__label">www.willowmereplace.com</span>
  </section>

</main>
</body>
</html>
```